Investment Advisor E-Newsletter Banner Design

I need a banner designed for an email newsletter that will be sent monthly to clients and prospects. We want to see designs that are elegant and use our logo well. The banner should be 922x150px and should go well with the www.bltvorna.com website. Should include Logo and email and phone number.

Target Market(s)

High net worth investors

Number of Pages Required

1 page

Requirements
Must have
• logo, place for email (info@bltvorna.com) and phone number (555-297-6184), colors and design that work well with www.bltvorna.com website

```html
<!DOCTYPE html>
<html lang="en">
<head>
<meta charset="utf-8">
<title>Bltvorna Capital – Newsletter Banner</title>
<link href="https://fonts.googleapis.com/css2?family=Libre+Baskerville&family=Roboto:wght@400&display=swap" rel="stylesheet">
<style>
  :root {
    --navy: #1f2a7a;
    --navy-deep: #161d5c;
    --brand-blue: #2a33a0;
    --white: #ffffff;
    --photo-dark: #23262d;
    --photo-mid: #4a4f5a;
    --photo-light: #7c808a;
  }
  html, body {
    margin: 0;
    padding: 0;
    overflow: hidden;
    background: var(--white);
  }
  .banner {
    position: relative;
    width: 1200px;
    height: 195px;
    overflow: hidden;
    background: var(--photo-dark);
  }
  .banner__photo {
    position: absolute;
    inset: 0;
    background:
      radial-gradient(ellipse 320px 140px at 760px 70px, rgba(160,165,175,0.35), transparent 70%),
      linear-gradient(100deg, var(--photo-mid) 0%, var(--photo-dark) 45%, var(--photo-mid) 75%, var(--photo-dark) 100%);
  }
  .banner__panel {
    position: absolute;
    left: 0;
    top: 0;
    width: 460px;
    height: 195px;
  }
  .brand {
    position: absolute;
    left: 34px;
    top: 58px;
    display: flex;
    align-items: center;
    gap: 16px;
  }
  .brand__mark {
    width: 58px;
    height: 58px;
    background: var(--brand-blue);
    flex: none;
  }
  .brand__name {
    font-family: "Libre Baskerville", serif;
    font-weight: 400;
    color: var(--brand-blue);
    font-size: 27px;
    line-height: 1.15;
  }
  .brand__name small {
    display: block;
    font-size: 15px;
    line-height: 1.5;
  }
  .tagline {
    position: absolute;
    left: 624px;
    top: 70px;
    margin: 0;
    font-family: "Libre Baskerville", serif;
    font-weight: 400;
    font-size: 29px;
    letter-spacing: 0.5px;
    color: var(--white);
  }
  .contact-bar {
    position: absolute;
    left: 628px;
    top: 140px;
    width: 572px;
    height: 55px;
    background: var(--navy);
    clip-path: polygon(14px 0, 100% 0, 100% 100%, 0 100%);
    display: flex;
    align-items: center;
    gap: 34px;
    padding-left: 24px;
    box-sizing: border-box;
    font-family: "Roboto", sans-serif;
    font-size: 22px;
    color: var(--white);
    text-transform: uppercase;
  }
  .contact-bar__item {
    display: flex;
    align-items: center;
    gap: 10px;
  }
  .contact-bar__icon {
    width: 22px;
    height: 22px;
    fill: var(--white);
  }
</style>
</head>
<body>
  <div class="banner">
    <div class="banner__photo" role="img" aria-label="Dark photograph of business people's hands discussing charts on a tablet at a desk"></div>

    <svg class="banner__panel" viewBox="0 0 460 195" aria-hidden="true">
      <polygon points="0,0 404,0 456,97.5 404,195 0,195" fill="var(--navy)"/>
      <polygon points="0,0 388,0 440,97.5 388,195 0,195" fill="var(--white)"/>
    </svg>

    <div class="brand">
      <div class="brand__mark"></div>
      <div class="brand__name">Bltvorna Capital<small>Advisory &amp; Research, Inc.</small></div>
    </div>

    <h1 class="tagline">EVIDENCE-BASED INVESTING</h1>

    <div class="contact-bar">
      <span class="contact-bar__item">
        <svg class="contact-bar__icon" viewBox="0 0 24 24" aria-hidden="true"><path d="M6.6 10.8c1.4 2.8 3.8 5.1 6.6 6.6l2.2-2.2c.3-.3.7-.4 1-.2 1.1.4 2.3.6 3.6.6.6 0 1 .4 1 1V20c0 .6-.4 1-1 1C10.6 21 3 13.4 3 4c0-.6.4-1 1-1h3.5c.6 0 1 .4 1 1 0 1.3.2 2.5.6 3.6.1.3 0 .7-.2 1L6.6 10.8z"/></svg>
        555-297-6184
      </span>
      <span class="contact-bar__item">
        <svg class="contact-bar__icon" viewBox="0 0 24 24" aria-hidden="true"><path d="M2 5h20v14H2z" fill="none"/><path d="M3 5h18c.6 0 1 .4 1 1v.4l-10 6.3L2 6.4V6c0-.6.4-1 1-1zm-1 3.7l10 6.3 10-6.3V18c0 .6-.4 1-1 1H3c-.6 0-1-.4-1-1V8.7z"/></svg>
        info@bltvorna.com
      </span>
    </div>
  </div>
</body>
</html>
```